-------------- 概要 -------------- 会社で従業員に配布するための、名刺デザイン を募集します。 -------------------------- 依頼内容 -------------------------- ・サイズ:91×55mm ・素材の用意(画像・文章等):添付のロゴを使用してデザインください ・デザイン内容: ー横書き、横置きでお願いします ー表面:社名、役職、氏名、住所(〒389-0742 長野県架空市青葉台7丁目3番15-905号) 、 携帯電話、メールアドレス(~~~@xq-v.co.jp)、ロゴ、HPのURL(https://www.xq-v.co.jp) ※( )の記載がない項目は仮置きでお願いできますでしょうか。 ー裏面:ロゴのみでよいと思っていますが、ぜひご意見、ご提案いただけると幸いです。 -------------------------- デザインイメージ -------------------------- ●ターゲット層: 企業で働く社会人向け(新人から部長層くらいまで)の研修を提供する会社です。直接の顧客は、その企業の人事部門となります。 ●雰囲気: 人事部門が相手となるため、信頼性と、社名にも込めた顧客のパートナーとして身近で温かみのあるイメージが伝わるとよいです。 コーポレートカラーは、【明るめの緑色】(添付の白抜きロゴの背景色)にしようと考えています。 研修での学習を通じて、人の成長が促されることを願っています。 また、会社が大事にしたいことを表すキーワードとしては、「共に」や「寄り添い」です。 ●ロゴの希望イメージの補足: 「伝統的⇔先進的」という選択項目は、先進的に近い方を選んでいますが 実際は「普遍的」というのも大事にしたいと思っています。 ただ、「伝統的」という言葉から想起されやすい”古さ”や”頑なさ”のようなイメージは 持ってほしくないと考えているため「先進的」にやや寄せました。 ●希望カラーの補足: 「緑系(安らぎ・平和・優しい)」選択しましたが、コーポレートカラーにする予定の 明るめの緑(黄緑、白抜きロゴの背景色)を使用していただきたいです。 ---------------- その他 ---------------- ※契約金額(税込)からシステム利用料を差し引いた金額が、ワーカーさまの受取金額となります その他ご質問等ありましたら、気軽にお問い合わせください。 ご応募をお待ちしております! |
以下のような要望に一番お応えいただいていたと感じたためです。
・表面については、肩書・名前・住所などの必要項目の記載が名刺右側にまとまっていたため、シンプルな印象や視認しやすい点がよかったです。
・また、表面において、ロゴも目立ちやすくよかったです。
・裏面についてはグラデーションや薄く白抜きしたロゴとのバランスがよく、シンプルさを保ちつつも、洗練された印象がよかったです。
全体的にシンプルでありつつも、古臭い感じではなく、先進的な印象も持てるデザインだったため、選択をさせていただきました。
素敵なデザインを提示いただきありがとうございました。
みなさま、ご提案をいただきありがとうございました。
どの案もこちらの要望にお応えいただいていたため、採用の決定については悩みました。
改めて、シンプルさと先進的(洗練された印象)のバランスのよさを最重視して選択をいたしました。

```html
<!DOCTYPE html>
<html lang="ja">
<head>
<meta charset="utf-8">
<title>XQ Vista 名刺デザイン</title>
<link rel="stylesheet" href="https://fonts.googleapis.com/css2?family=Noto+Sans+JP:wght@400;500;700&family=Noto+Serif+JP:wght@500;600&display=swap">
<style>
  :root {
    --board-light: #d4d4d4;
    --board-dark: #a8a8a8;
    --green: #3f8f24;
    --green-bright: #8cc63f;
    --green-deep: #2f7a1c;
    --cream: #fbfbf1;
    --mint: #eff3dc;
    --charcoal: #343434;
    --ink: #333;
    --muted: #777;
    --grey-text: #8a8a8a;
  }
  * { margin: 0; padding: 0; box-sizing: border-box; }
  html, body { width: 1200px; height: 526px; overflow: hidden; }
  body {
    background: radial-gradient(ellipse at 50% 40%, var(--board-light), var(--board-dark));
    font-family: "Noto Sans JP", sans-serif;
    position: relative;
  }
  .card {
    position: absolute;
    width: 340px;
    height: 210px;
    box-shadow: 0 4px 10px rgba(0,0,0,.35);
    overflow: hidden;
  }
  .col-1 { left: 36px; }
  .col-2 { left: 430px; }
  .col-3 { left: 824px; }
  .row-front { top: 24px; }
  .row-back { top: 262px; }

  /* Front */
  .front { padding: 14px 20px; color: var(--ink); }
  .front.cream { background: var(--cream); }
  .front.mint { background: var(--mint); }
  .front.dark { background: var(--charcoal); color: var(--grey-text); }
  .brand { display: flex; align-items: center; gap: 6px; }
  .brand-dot { width: 16px; height: 16px; border-radius: 50%; background: var(--green-bright); }
  .mint .brand-dot { background: var(--green); }
  .dark .brand-dot { background: #6d6d6d; }
  .brand-name { font-size: 16px; font-weight: 500; color: var(--green); letter-spacing: .2px; }
  .cream .brand-name { color: var(--green-deep); }
  .dark .brand-name { color: #9a9a9a; }
  .url { font-size: 7px; margin: 0 0 0 22px; color: var(--green); }
  .dark .url { color: #888; }
  .role { font-size: 6.5px; color: var(--muted); margin-top: 38px; }
  .dark .role { color: #777; }
  .name-line { display: flex; align-items: center; margin-top: 4px; }
  .name-ja { font-family: "Noto Serif JP", serif; font-weight: 600; font-size: 15px; letter-spacing: 4px; }
  .divider { width: 2px; height: 13px; background: var(--green); margin: 0 8px 0 6px; }
  .dark .divider { background: #777; }
  .name-en { font-family: "Noto Serif JP", serif; font-size: 9px; letter-spacing: 1px; color: var(--green); }
  .cream .name-en { color: var(--ink); }
  .dark .name-en { color: #999; }
  .company { font-size: 7.5px; font-weight: 700; margin-top: 22px; }
  .contact { font-size: 6.3px; line-height: 1.7; margin-top: 2px; }
  .contact span { font-weight: 700; }
  .dark .contact { color: #6f6f6f; }

  /* Back */
  .back { display: flex; flex-direction: column; align-items: center; justify-content: center; }
  .back.green { background: radial-gradient(ellipse at 50% 45%, #a8d433 0%, var(--green-bright) 40%, #4e9a25 100%); }
  .back.grey { background: radial-gradient(ellipse at 50% 45%, #6e6e6e 0%, #4a4a4a 50%, #2a2a2a 100%); }
  .back .brand-dot { width: 28px; height: 28px; background: #fff; margin-bottom: 8px; }
  .back .brand-name { color: #fff; font-size: 18px; }
</style>
</head>
<body>
  <article class="card front cream col-1 row-front">
    <div class="brand"><span class="brand-dot"></span><span class="brand-name">XQ Vista</span></div>
    <p class="url">https://www.xq-v.co.jp</p>
    <p class="role">代表取締役</p>
    <div class="name-line"><span class="name-ja">青葉 花子</span><span class="divider"></span><span class="name-en">HANAKO AOBA</span></div>
    <p class="company">株式会社 XQ Vista</p>
    <p class="contact">〒389-0742 長野県架空市青葉台7丁目3番15-905号<br><span>TEL</span> 026-555-0147 / <span>FAX</span> 026-555-0148<br><span>Mail</span> h.aoba2022@xq-v.co.jp</p>
  </article>

  <article class="card front mint col-2 row-front">
    <div class="brand"><span class="brand-dot"></span><span class="brand-name">XQ Vista</span></div>
    <p class="url">https://www.xq-v.co.jp</p>
    <p class="role">代表取締役</p>
    <div class="name-line"><span class="name-ja">青葉 花子</span><span class="divider"></span><span class="name-en">HANAKO AOBA</span></div>
    <p class="company">株式会社 XQ Vista</p>
    <p class="contact">〒389-0742 長野県架空市青葉台7丁目3番15-905号<br><span>TEL</span> 026-555-0147 / <span>FAX</span> 026-555-0148<br><span>Mail</span> h.aoba2022@xq-v.co.jp</p>
  </article>

  <article class="card front dark col-3 row-front">
    <div class="brand"><span class="brand-dot"></span><span class="brand-name">XQ Vista</span></div>
    <p class="url">https://www.xq-v.co.jp</p>
    <p class="role">代表取締役</p>
    <div class="name-line"><span class="name-ja">青葉 花子</span><span class="divider"></span><span class="name-en">HANAKO AOBA</span></div>
    <p class="company">株式会社 XQ Vista</p>
    <p class="contact">〒389-0742 長野県架空市青葉台7丁目3番15-905号<br><span>TEL</span> 026-555-0147 / <span>FAX</span> 026-555-0148<br><span>Mail</span> h.aoba2022@xq-v.co.jp</p>
  </article>

  <article class="card back green col-1 row-back">
    <span class="brand-dot"></span><span class="brand-name">XQ Vista</span>
  </article>
  <article class="card back green col-2 row-back">
    <span class="brand-dot"></span><span class="brand-name">XQ Vista</span>
  </article>
  <article class="card back grey col-3 row-back">
    <span class="brand-dot"></span><span class="brand-name">XQ Vista</span>
  </article>
</body>
</html>
```